Advertisements needed for new pub to expand clientele

I need a few different advert. done for my business, can use the same background for all, that covers the following

- New Late Night Menu with Back To School Late Night Prices Thursday-Saturday while bar is open

- $25 gift card to be drawn on September 30th with Liking our facebook page, sharing the ad., and using the hashtag #PackTheGrill

- Happy Hour Pints $7 & Buy 3 Pints get a free Pretzel Bites between 4:00-5:00 PM

http://www.portkestleybrew.com/

https://www.facebook.com/PtKestleyPub/

Restaurant Diners

Business

• Logo of Pub
• Key information in description for each

```html
<!DOCTYPE html>
<html lang="en">
<head>
<meta charset="utf-8">
<title>Pt. Kestley Pub – Gift Card Draw</title>
<link rel="stylesheet" href="https://fonts.googleapis.com/css2?family=Montserrat:wght@300;400;600;700;800;900&family=Raleway:wght@200;300&display=swap">
<style>
  :root {
    --promo-red: #e8242b;
    --ink-black: #0b0b0b;
    --paper-white: #ffffff;
    --soft-grey: #d6d6d6;
    --button-blue: #3b5a9a;
    --button-light: #eef2fa;
  }
  html, body {
    margin: 0;
    padding: 0;
    overflow: hidden;
    background: var(--ink-black);
  }
  .ad {
    position: relative;
    width: 1200px;
    height: 850px;
    overflow: hidden;
    font-family: "Montserrat", sans-serif;
    color: var(--paper-white);
  }

  /* ---------- Promo side ---------- */
  .promo {
    position: absolute;
    left: 0; top: 0;
    width: 600px; height: 850px;
  }
  .promo__photo {
    position: absolute;
    inset: 0;
    background:
      linear-gradient(180deg, rgba(0,0,0,0) 60%, rgba(60,40,25,.55) 100%),
      radial-gradient(ellipse at 55% 70%, #b9bcbf 0%, #85898d 35%, transparent 70%),
      linear-gradient(180deg, #6c6f73 0%, #7d8084 40%, #8e8f8f 65%, #5b4a3a 100%);
  }
  .banner {
    position: absolute;
    left: 0;
    background: var(--promo-red);
    clip-path: polygon(0 0, 100% 0, 94% 50%, 100% 100%, 0 100%);
  }
  .banner--win {
    top: 28px; width: 392px; height: 126px;
  }
  .banner--win h1 {
    margin: 0;
    position: absolute;
    left: 66px; top: 6px;
    font-size: 100px;
    font-weight: 900;
    letter-spacing: 1px;
    line-height: 1.1;
  }
  .banner--prize {
    top: 168px; width: 390px; height: 104px;
  }
  .prize__amount {
    position: absolute;
    left: 42px; top: 4px;
    font-size: 76px;
    font-weight: 800;
    line-height: 1.2;
  }
  .prize__amount sup {
    font-size: 36px;
    vertical-align: 30px;
    margin-right: 2px;
  }
  .prize__label {
    position: absolute;
    left: 212px; top: 47px;
    font-size: 28px;
    font-weight: 700;
  }
  .steps {
    position: absolute;
    left: 104px; top: 306px;
    margin: 0; padding: 0;
    list-style: none;
    font-size: 25px;
    font-weight: 700;
    line-height: 38px;
    text-shadow: 0 1px 3px rgba(0,0,0,.5);
  }
  .steps li span {
    display: inline-block;
    width: 26px; height: 26px;
    margin-right: 8px;
    border-radius: 50%;
    background: var(--paper-white);
    color: var(--ink-black);
    font-size: 17px;
    text-align: center;
    line-height: 26px;
    vertical-align: 2px;
    text-shadow: none;
  }
  .steps .hashtag { padding-left: 36px; }

  .social-btn {
    position: absolute;
    display: flex;
    align-items: center;
    box-sizing: border-box;
    font-family: "Montserrat", sans-serif;
  }
  .social-btn--like {
    left: 117px; top: 492px;
    width: 125px; height: 53px;
    border: 2px solid var(--button-blue);
    border-radius: 8px;
    background: var(--button-light);
    color: var(--button-blue);
    font-size: 26px;
    font-weight: 600;
    padding-left: 12px;
    gap: 10px;
  }
  .social-btn--like i {
    width: 22px; height: 22px;
    background: var(--button-blue);
    border-radius: 50%;
  }
  .social-btn--share {
    left: 120px; top: 564px;
    width: 146px; height: 33px;
    background: var(--button-blue);
    border-radius: 3px;
    color: var(--paper-white);
    font-size: 11px;
    padding-left: 8px;
    gap: 8px;
  }
  .social-btn--share i {
    width: 12px; height: 12px;
    background: var(--paper-white);
  }
  .social-btn--tag {
    left: 118px; top: 614px;
    width: 64px; height: 56px;
    background: var(--button-blue);
    border-radius: 3px;
    justify-content: center;
    color: var(--paper-white);
    font-size: 30px;
    font-weight: 700;
  }

  .banner--draw {
    top: 695px; width: 392px; height: 110px;
  }
  .draw__label {
    position: absolute;
    left: 32px; top: 22px;
    font-size: 23px;
    font-weight: 400;
    letter-spacing: 2.5px;
  }
  .draw__date {
    position: absolute;
    left: 31px; top: 55px;
    font-size: 27px;
    font-weight: 700;
    letter-spacing: 1px;
  }

  /* ---------- Info side ---------- */
  .info {
    position: absolute;
    left: 600px; top: 0;
    width: 600px; height: 850px;
    background: var(--ink-black);
  }
  .brand {
    position: absolute;
    left: 0; right: 0; top: 118px;
    display: flex;
    flex-direction: column;
    align-items: center;
    gap: 22px;
  }
  .brand__dot {
    width: 70px; height: 70px;
    border: 3px solid var(--paper-white);
    border-radius: 50%;
  }
  .brand__name {
    font-family: "Montserrat", sans-serif;
    font-weight: 400;
    font-size: 34px;
    letter-spacing: 3px;
  }
  .tagline {
    position: absolute;
    left: 0; right: 0; top: 340px;
    text-align: center;
    font-family: "Raleway", sans-serif;
    font-weight: 300;
    font-size: 20px;
    letter-spacing: 1.5px;
    color: var(--soft-grey);
  }
  .rule {
    position: absolute;
    left: 100px;
    width: 402px; height: 4px;
    background: var(--paper-white);
  }
  .rule--top { top: 413px; }
  .rule--bottom { top: 545px; }
  .contact {
    position: absolute;
    left: 195px; top: 438px;
    font-size: 20px;
    font-weight: 300;
    line-height: 27px;
    font-style: normal;
  }
  .contact svg { vertical-align: -3px; margin-right: 4px; }
  .hours {
    position: absolute;
    left: 228px;
    font-weight: 300;
  }
  .hours h2 {
    margin: 0 0 10px;
    font-size: 17px;
    font-weight: 400;
    letter-spacing: .5px;
  }
  .hours p {
    margin: 0;
    font-size: 16px;
    line-height: 23px;
  }
  .hours--food { top: 611px; }
  .hours--bar { top: 714px; }
  .hours__icon {
    position: absolute;
    left: -54px;
  }
  .hours--food .hours__icon { top: 34px; }
  .hours--bar .hours__icon { top: 28px; }
</style>
</head>
<body>
<main class="ad">
  <section class="promo">
    <div class="promo__photo" role="img" aria-label="Photo of the pub's stainless beer tap tower with assorted tap handles against a grey wall"></div>

    <div class="banner banner--win"><h1>WIN!</h1></div>
    <div class="banner banner--prize">
      <span class="prize__amount"><sup>$</sup>25</span>
      <span class="prize__label">Gift Card</span>
    </div>

    <ol class="steps">
      <li><span>1</span>Like our Chatterbook Page</li>
      <li><span>2</span>Share or Chatterbook Page</li>
      <li><span>3</span>Use the hashtag</li>
      <li class="hashtag">#PackTheGrill</li>
    </ol>

    <div class="social-btn social-btn--like"><i></i>Like</div>
    <div class="social-btn social-btn--share"><i></i>Share on Chatterbook</div>
    <div class="social-btn social-btn--tag">#</div>

    <div class="banner banner--draw">
      <span class="draw__label">Draw Date:</span>
      <span class="draw__date">September 30, 2017</span>
    </div>
  </section>

  <section class="info">
    <div class="brand">
      <div class="brand__dot"></div>
      <div class="brand__name">Pt. Kestley Pub</div>
    </div>

    <p class="tagline">LOCALLY SOURCED × CRAFTED WITH LOVE</p>

    <div class="rule rule--top"></div>
    <address class="contact">
      47 Larkin Street<br>
      Harbour Cove, NL A1C3Y4<br>
      <svg width="18" height="18" viewBox="0 0 18 18" aria-hidden="true"><circle cx="9" cy="9" r="8" fill="none" stroke="#fff" stroke-width="1.3"/><path d="M6 4.5c-1 1-1 3 1 5.5s4 3.5 5 2.5l-1.5-1.8-1.2.6c-1-.6-2-1.8-2.4-2.8l.8-1.1z" fill="#fff"/></svg>(709) 555-0182
    </address>
    <div class="rule rule--bottom"></div>

    <div class="hours hours--food">
      <svg class="hours__icon" width="36" height="40" viewBox="0 0 36 40" aria-hidden="true">
        <path d="M4 38 L30 6" stroke="#fff" stroke-width="3" stroke-linecap="round"/>
        <path d="M32 38 L10 10" stroke="#fff" stroke-width="3" stroke-linecap="round"/>
        <path d="M10 10 L4 2 M7 13 L1 6 M13 8 L7 0" stroke="#fff" stroke-width="2" stroke-linecap="round"/>
        <path d="M30 6 Q36 0 33 10 L28 12 Z" fill="#fff"/>
      </svg>
      <h2>FOOD HOURS</h2>
      <p>Tu-Th 11:30-2 &amp; 5-9:30<br>F-Sa&nbsp; 11:30-3 &amp; 4-10</p>
    </div>

    <div class="hours hours--bar">
      <svg class="hours__icon" width="36" height="48" viewBox="0 0 36 48" aria-hidden="true">
        <path d="M18 4 q4 3 0 6 q-4 3 0 6 q4 3 0 6 q-4 3 0 6 L18 34" fill="none" stroke="#fff" stroke-width="2"/>
        <rect x="6" y="34" width="24" height="6" rx="3" fill="none" stroke="#fff" stroke-width="2"/>
        <circle cx="5" cy="40" r="4" fill="none" stroke="#fff" stroke-width="2"/>
        <circle cx="31" cy="40" r="4" fill="none" stroke="#fff" stroke-width="2"/>
      </svg>
      <h2>BAR HOURS</h2>
      <p>Tu-Th 4-11<br>F-Sa&nbsp; 4–1</p>
    </div>
  </section>
</main>
</body>
</html>
```